Business Card Design

we specialise in supply of custom uniforms - teamwear to Schools and sporting clubs, see our website: www.harbourkitcove.com.au, our main corporate colour is black and white, with small amount of gold/yellow

Industry/Entity Type

Business

Contact Information for Business Card

Harbour Kit Cove
Travis Okafor
Ph 03 6218 5097
Mobile 0462 318 740
email: travis@harbourkitcove.com.au
www.harbourkitcove.com.au
like us on facebook

Requirements
Must have
• modern look & feel

```html
<!DOCTYPE html>
<html lang="en">
<head>
<meta charset="utf-8">
<title>Harbour Kit Cove – Business Card</title>
<link rel="stylesheet" href="https://fonts.googleapis.com/css2?family=Arimo:wght@400;700&family=Open+Sans:wght@400;600&display=swap">
<style>
  :root {
    --backdrop: #d9d9d9;
    --card-dark: #0e0e0e;
    --card-mid: #1b1b1b;
    --gold: #f7d320;
    --gold-deep: #f0c814;
    --ink: #141414;
    --paper: #f4f4f4;
  }
  * { margin: 0; padding: 0; box-sizing: border-box; }
  html, body {
    width: 1200px; height: 900px; overflow: hidden;
    background: var(--backdrop);
  }
  .card {
    position: absolute; left: 100px; top: 164px;
    width: 1000px; height: 572px;
    background: linear-gradient(160deg, var(--card-mid) 0%, var(--card-dark) 55%, var(--card-mid) 100%);
    box-shadow: 0 18px 40px rgba(0,0,0,.35);
    overflow: hidden;
    font-family: "Open Sans", Arial, sans-serif;
    color: var(--paper);
  }
  .brand-mark {
    position: absolute; right: 110px; top: 58px;
    display: flex; align-items: center; gap: 10px;
    font-family: "Arimo", Arial, sans-serif; font-weight: 700;
    font-size: 20px; color: var(--paper);
  }
  .brand-mark .dot { width: 14px; height: 14px; border-radius: 50%; background: var(--paper); }
  .gold-band {
    position: absolute; left: 0; right: 0; top: 212px; height: 132px;
    background: linear-gradient(180deg, var(--gold) 0%, var(--gold-deep) 100%);
  }
  .company-name {
    position: absolute; right: 86px; top: 160px;
    font-family: "Arimo", Arial, sans-serif; font-weight: 700;
    font-size: 44px; letter-spacing: -0.5px; color: var(--gold);
  }
  .person-name {
    position: absolute; right: 100px; top: 226px;
    font-family: "Arimo", Arial, sans-serif; font-weight: 400;
    font-size: 28px; color: var(--ink);
  }
  .phones, .links { position: absolute; list-style: none; }
  .phones { left: 690px; top: 372px; }
  .links { left: 58px; top: 444px; }
  .phones li, .links li {
    display: flex; align-items: center; gap: 12px;
    font-size: 16px; letter-spacing: .6px; height: 34px;
  }
  .icon { width: 18px; height: 18px; flex: none; }
</style>
</head>
<body>
  <main class="card">
    <div class="brand-mark"><span class="dot"></span>Harbour Kit Cove</div>

    <div class="gold-band"></div>
    <h1 class="company-name">Harbour Kit Cove</h1>
    <p class="person-name">Travis Okafor</p>

    <ul class="phones">
      <li>
        <svg class="icon" viewBox="0 0 18 18"><rect x="5" y="2" width="8" height="14" rx="1.5" fill="none" stroke="#f7d320" stroke-width="1.6"/><line x1="8" y1="13.5" x2="10" y2="13.5" stroke="#f7d320" stroke-width="1.4"/></svg>
        0462 318 740
      </li>
      <li>
        <svg class="icon" viewBox="0 0 18 18"><path d="M4 3l3 0 1 4-2 1c1 2 2 3 4 4l1-2 4 1 0 3c-7 1-12-4-11-11z" fill="#f7d320"/></svg>
        03 6218 5097
      </li>
    </ul>

    <ul class="links">
      <li>
        <svg class="icon" viewBox="0 0 18 18"><circle cx="9" cy="9" r="7.5" fill="none" stroke="#f7d320" stroke-width="1.5"/><ellipse cx="9" cy="9" rx="3.2" ry="7.5" fill="none" stroke="#f7d320" stroke-width="1.2"/><line x1="1.5" y1="9" x2="16.5" y2="9" stroke="#f7d320" stroke-width="1.2"/></svg>
        www.harbourkitcove.com.au
      </li>
      <li>
        <svg class="icon" viewBox="0 0 18 18"><rect x="1" y="1" width="16" height="16" rx="2" fill="#f7d320"/></svg>
        / harbourkitcove
      </li>
      <li>
        <svg class="icon" viewBox="0 0 18 18"><circle cx="9" cy="9" r="8.5" fill="#f7d320"/><rect x="4.5" y="6" width="9" height="6.5" fill="none" stroke="#141414" stroke-width="1.2"/><path d="M4.5 6l4.5 4 4.5-4" fill="none" stroke="#141414" stroke-width="1.2"/></svg>
        travis@harbourkitcove.com.au
      </li>
    </ul>
  </main>
</body>
</html>
```